Tree Service Billboard 20x8 ft

We need a billboard design for a tree service company.
The billboard is 20ft x 8 ft so we need a design that is capable to stretching to those dimensions without loosing quality.
I have attached a series of images.
Image 1- Simply a billboard that I think looks good that I would like you to use for inspiration. I am aiming for the same format only no color in the wording, just black white, or gray. I like the the trees in the background, the logo placed to the left, and wording on the right.
Image 2- Current Logo I would like to the left of the billboard
Image 3- Another format of current logo if needed.
Image 4- A drawn out design template
Image 5- Another drawn out design template

Specific things I am looking for
-The contact number to be the largest thing on the design
-The logo on the design
-Key points to the design to say:
Tree Removal
Tree Trimming
Land Development
Stump Grinding
Storm Response
Insured
Free Bids
-The facebook logo
-The Google Logo

```html
<!DOCTYPE html>
<html lang="en">
<head>
<meta charset="utf-8">
<title>Tree Service Billboard 20x8 ft</title>
<link rel="stylesheet" href="https://fonts.googleapis.com/css2?family=Anton&family=Montserrat:wght@500;700&family=Oswald:wght@600;700&display=swap">
<style>
  :root {
    --page-bg: #f2f2f2;
    --ink: #000000;
    --paper: #ffffff;
    --mist: #c9c9cc;
    --mid-gray: #8a8a8e;
    --ring-gray: #6e6e6e;
  }
  html, body {
    margin: 0;
    padding: 0;
    width: 1200px;
    height: 833px;
    overflow: hidden;
    background: var(--page-bg);
  }
  .presentation {
    position: relative;
    width: 1200px;
    height: 833px;
  }
  .presentation-title {
    position: absolute;
    top: 148px;
    left: 0;
    width: 1200px;
    margin: 0;
    text-align: center;
    font-family: "Montserrat", sans-serif;
    font-weight: 500;
    font-size: 46px;
    letter-spacing: 1px;
    color: var(--ink);
  }
  .billboard {
    position: absolute;
    left: 63px;
    top: 251px;
    width: 1074px;
    height: 430px;
  }
  .brand-name, .phone-number {
    font-family: "Oswald", sans-serif;
    font-weight: 700;
    fill: var(--paper);
  }
  .service-item {
    font-family: "Anton", sans-serif;
    font-size: 43px;
    fill: var(--ink);
  }
  .badge-label {
    font-family: "Montserrat", sans-serif;
    font-weight: 700;
    font-size: 23px;
    fill: var(--paper);
  }
</style>
</head>
<body>
<main class="presentation">
  <h1 class="presentation-title">TREE SERVICE BILLBOARD 20X8 FT</h1>

  <svg class="billboard" viewBox="0 0 1074 430" xmlns="http://www.w3.org/2000/svg">
    <defs>
      <linearGradient id="forest-sky" x1="0" y1="0" x2="0" y2="1">
        <stop offset="0" stop-color="#d6d6d8"/>
        <stop offset="0.35" stop-color="#9a9a9e"/>
        <stop offset="0.7" stop-color="#1a1a1a"/>
        <stop offset="1" stop-color="#000000"/>
      </linearGradient>
      <linearGradient id="forest-shade" x1="0" y1="0" x2="1" y2="0">
        <stop offset="0" stop-color="#000" stop-opacity="0.75"/>
        <stop offset="0.35" stop-color="#000" stop-opacity="0.2"/>
        <stop offset="0.7" stop-color="#000" stop-opacity="0.35"/>
        <stop offset="1" stop-color="#000" stop-opacity="0"/>
      </linearGradient>
      <radialGradient id="stump-tone" cx="0.5" cy="0.5" r="0.5">
        <stop offset="0" stop-color="#9a9a9a"/>
        <stop offset="1" stop-color="#2a2a2a"/>
      </radialGradient>
    </defs>

    <!-- base -->
    <rect class="billboard-base" width="1074" height="430" fill="var(--ink)"/>

    <!-- forest backdrop -->
    <g role="img" aria-label="Misty pine forest silhouettes in grey tones">
      <rect x="0" y="0" width="1074" height="300" fill="url(#forest-sky)"/>
      <rect x="0" y="0" width="1074" height="300" fill="url(#forest-shade)"/>
    </g>

    <!-- services panel -->
    <circle class="panel-edge" cx="962" cy="220" r="266" fill="var(--ring-gray)"/>
    <circle class="services-panel" cx="954" cy="216" r="260" fill="var(--paper)"/>
    <rect x="1000" y="0" width="74" height="430" fill="var(--paper)"/>

    <!-- brand mark -->
    <g class="brand-mark">
      <circle cx="268" cy="122" r="89" fill="var(--paper)"/>
      <circle cx="268" cy="122" r="81" fill="none" stroke="var(--ink)" stroke-width="4"/>
    </g>
    <text class="brand-name" x="87" y="268" font-size="56" textLength="377" lengthAdjust="spacingAndGlyphs">HALE’S TREE SERVICE</text>

    <!-- contact -->
    <text class="phone-number" x="85" y="390" font-size="80" textLength="426" lengthAdjust="spacingAndGlyphs">417-555-0148</text>
    <g class="social-links" fill="none" stroke="var(--paper)" stroke-width="3">
      <circle cx="546" cy="361" r="18"/>
      <circle cx="600" cy="361" r="18"/>
    </g>

    <!-- services list -->
    <g class="services-list" text-anchor="end">
      <text class="service-item" x="1004" y="94" textLength="201" lengthAdjust="spacingAndGlyphs">TREE REMOVAL</text>
      <text class="service-item" x="1004" y="148" textLength="212" lengthAdjust="spacingAndGlyphs">TREE TRIMMING</text>
      <text class="service-item" x="1004" y="202" textLength="277" lengthAdjust="spacingAndGlyphs">LAND DEVELOPMENT</text>
      <text class="service-item" x="1004" y="256" textLength="232" lengthAdjust="spacingAndGlyphs">STUMP GRINDING</text>
      <text class="service-item" x="1004" y="310" textLength="243" lengthAdjust="spacingAndGlyphs">STORM RESPONSE</text>
    </g>
    <g class="service-bullets" role="img" aria-label="Tree stump cross-section bullets" stroke="var(--ink)" stroke-width="1.5" fill="url(#stump-tone)">
      <circle cx="1024" cy="78" r="12"/>
      <circle cx="1024" cy="132" r="12"/>
      <circle cx="1024" cy="186" r="12"/>
      <circle cx="1024" cy="240" r="12"/>
      <circle cx="1024" cy="294" r="12"/>
    </g>

    <!-- insured badge -->
    <g class="insured-badge">
      <rect x="866" y="336" width="172" height="61" rx="30.5" fill="var(--ink)" stroke="var(--paper)" stroke-width="2"/>
      <text class="badge-label" x="955" y="364" text-anchor="middle">FULLY</text>
      <text class="badge-label" x="955" y="387" text-anchor="middle">INSURED</text>
      <path d="M817 336 Q850 334 851 326 Q852 334 885 336 L885 376 Q885 398 851 409 Q817 398 817 376 Z" fill="var(--ink)" stroke="var(--mid-gray)" stroke-width="2"/>
      <path d="M832 366 L846 380 L871 350" fill="none" stroke="var(--paper)" stroke-width="6" stroke-linecap="round" stroke-linejoin="round"/>
    </g>
  </svg>
</main>
</body>
</html>
```